Business Card Design For Marketing Agnecy LVT

Need business card design for marketing agency.

Dorian Pell
President, CEO
1-555-304-2917
dorian@lumenvaletrewards.net
www.LumenValeTrewards.biz

Back Side:
Boost Sales Using Rewards, Incentives & Giveaways
Get A Free Sample Package

Target Market(s)

B2B

Industry/Entity Type

Marketing

Contact Information for Business Card

Dorian Pell
President, CEO
1-555-304-2917

Back Side:
Get A Free Sample Package

Please note that my current url is OLD DESIGN. I am working on new design and want the business card to match color themes at least on new site. Here is the demo link for new site so you can see the colors I use, etc.

http://pagekilnstudio.example/qx/dorian/lvt_final/index.html

Requirements
Must have
• Please note that my current url is OLD DESIGN. I am working on new design and want the business card to match color themes at least on new site. Here is the demo link for new site so you can see the colors I use, etc.

Nice to have

Should not have

```html
<!DOCTYPE html>
<html lang="en">
<head>
<meta charset="utf-8">
<title>LVT Business Card</title>
<link rel="stylesheet" href="https://fonts.googleapis.com/css2?family=Lato:ital,wght@0,400;0,700;0,900;1,700&display=swap">
<style>
  :root {
    --page-bg: #e4e6e9;
    --card-white: #ffffff;
    --brand-blue: #2479c6;
    --brand-blue-dark: #1a5a99;
    --ink-navy: #1d3f6e;
    --ink-grey: #7d7f82;
    --ink-dark: #1c1c1c;
  }
  * { margin: 0; padding: 0; box-sizing: border-box; }
  html, body { width: 1200px; height: 926px; overflow: hidden; }
  body {
    background: var(--page-bg);
    font-family: "Lato", sans-serif;
    position: relative;
  }
  .card {
    position: absolute;
    left: 250px;
    width: 700px;
    height: 400px;
    background: var(--card-white);
    box-shadow: 0 6px 18px rgba(0,0,0,0.18);
    overflow: hidden;
  }
  .card--front { top: 42px; }
  .card--back { top: 484px; }

  .brand-mark {
    display: flex;
    align-items: center;
    gap: 10px;
  }
  .brand-mark__square {
    width: 26px; height: 26px;
    background: var(--brand-blue);
  }
  .brand-mark__name {
    font-weight: 900;
    font-size: 54px;
    letter-spacing: 2px;
    color: var(--brand-blue);
    line-height: 1;
  }

  /* front */
  .card--front .brand-mark { position: absolute; left: 48px; top: 40px; }
  .holder {
    position: absolute;
    right: 48px;
    top: 82px;
    text-align: right;
  }
  .holder__name {
    font-size: 34px;
    color: var(--brand-blue);
    text-transform: uppercase;
    letter-spacing: 0.5px;
    line-height: 1.05;
  }
  .holder__name strong { font-weight: 700; color: var(--brand-blue-dark); }
  .holder__title {
    font-size: 26px;
    color: var(--ink-grey);
    text-transform: uppercase;
    letter-spacing: 0.5px;
  }
  .holder__tab {
    position: absolute;
    right: 0; top: 110px;
    width: 28px; height: 52px;
    background: var(--brand-blue);
  }
  .contact {
    position: absolute;
    left: 48px;
    bottom: 70px;
    list-style: none;
    font-size: 21px;
    color: var(--ink-navy);
    line-height: 1.3;
  }
  .contact b { font-weight: 700; font-style: italic; }
  .footer-band {
    position: absolute;
    left: 0; right: 0; bottom: 0;
    height: 22px;
    display: flex;
    gap: 4px;
  }
  .footer-band span {
    flex: 1;
    background: linear-gradient(180deg, var(--brand-blue) 0%, var(--brand-blue-dark) 100%);
  }

  /* back */
  .card--back .brand-mark {
    position: absolute;
    left: 0; right: 0; top: 56px;
    justify-content: center;
  }
  .card--back .brand-mark__name { font-size: 66px; }
  .offer-band {
    position: absolute;
    left: 0; right: 0; top: 168px;
    height: 112px;
    background: var(--brand-blue);
    color: var(--card-white);
    display: flex;
    flex-direction: column;
    justify-content: center;
    align-items: center;
    font-weight: 700;
    font-size: 24px;
    letter-spacing: 0.8px;
    line-height: 1.3;
  }
  .site {
    position: absolute;
    left: 0; right: 0; top: 306px;
    text-align: center;
    font-weight: 700;
    font-size: 17px;
    letter-spacing: 2.5px;
    color: var(--ink-dark);
  }
</style>
</head>
<body>

  <section class="card card--front" aria-label="Business card front">
    <div class="brand-mark">
      <span class="brand-mark__square"></span>
      <span class="brand-mark__name">LVT</span>
    </div>
    <div class="holder">
      <p class="holder__name">Dorian <strong>Pell</strong></p>
      <p class="holder__title">President, CEO</p>
    </div>
    <span class="holder__tab"></span>
    <ul class="contact">
      <li><b>telephone:</b> 1-555-304-2917</li>
      <li><b>web:</b> LumenValeTrewards.biz</li>
      <li><b>email:</b> dorian@lumenvaletrewards.net</li>
    </ul>
    <div class="footer-band"><span></span><span></span><span></span></div>
  </section>

  <section class="card card--back" aria-label="Business card back">
    <div class="brand-mark">
      <span class="brand-mark__square"></span>
      <span class="brand-mark__name">LVT</span>
    </div>
    <div class="offer-band">
      <p>Boost Sales Using Rewards, Incentives &amp; Giveaways</p>
      <p>Get A Free Sample Package</p>
    </div>
    <p class="site">www.LumenValeTrewards.biz</p>
  </section>

</body>
</html>
```